Brackenfield Prime Healthcare Needs a Business Card Design

We need a business card design for a company based in Shorewood IL called "Brackenfield Prime Healthcare". We provide an integrated medical model involving chiropractic, trigger point injections and other medical services in one location. I have attached our logo to this with the colors being in the puzzle design of the logo. We are looking for a great design that will WOW those around us but also be able to communicate our information easily

Industry/Entity Type

Medical

Contact Information for Business Card

This is a integrated Medical office featuring numerous services to clients in the office.

Requirements
Must have
• Logo

```html
<!DOCTYPE html>
<html lang="en">
<head>
<meta charset="utf-8">
<title>Brackenfield Prime Healthcare – Business Card</title>
<link href="https://fonts.googleapis.com/css2?family=Open+Sans:wght@400;600;700&family=Cinzel:wght@400&display=swap" rel="stylesheet">
<style>
  :root {
    --page: #eeece8;
    --card: #f4f4f4;
    --card-edge: #e2e2e2;
    --blue: #6f98cc;
    --purple: #6a4fa3;
    --brand: #2f7fb8;
    --brand-mark: #f0802a;
    --white: #ffffff;
  }
  * { margin: 0; padding: 0; box-sizing: border-box; }
  html, body { width: 1200px; height: 899px; overflow: hidden; }
  body {
    background: var(--page);
    font-family: "Open Sans", Arial, sans-serif;
    position: relative;
  }
  .card {
    position: absolute;
    left: 290px;
    width: 620px;
    height: 354px;
    background: linear-gradient(135deg, var(--white), var(--card) 60%, var(--card-edge));
    box-shadow: 0 6px 18px rgba(0,0,0,0.18);
    overflow: hidden;
  }
  .card--front { top: 62px; }
  .card--back { top: 476px; }

  .brand {
    position: absolute;
    display: flex;
    align-items: center;
    gap: 12px;
  }
  .brand__square {
    width: 38px; height: 38px;
    background: var(--brand-mark);
    flex: none;
  }
  .brand__name {
    font-family: "Cinzel", Georgia, serif;
    color: var(--brand);
    font-size: 24px;
    line-height: 1.1;
    letter-spacing: 0.5px;
  }
  .card--front .brand { left: 50%; top: 50%; transform: translate(-50%, -50%); }
  .card--back .brand { left: 330px; top: 128px; }
  .card--back .brand__name { font-size: 19px; }
  .card--back .brand__square { width: 30px; height: 30px; }

  .back__wave { position: absolute; inset: 0; }

  .person {
    position: absolute;
    left: 34px; top: 40px;
    color: var(--white);
  }
  .person__name { font-size: 19px; font-weight: 700; }
  .person__role { font-size: 14px; margin-top: 2px; }

  .contacts {
    position: absolute;
    left: 34px; bottom: 30px;
    list-style: none;
    color: var(--white);
    font-size: 12px;
    line-height: 1.45;
  }
  .contacts li { display: flex; align-items: flex-start; gap: 7px; }
  .contacts svg { flex: none; margin-top: 2px; }
</style>
</head>
<body>

<section class="card card--front" aria-label="Card front">
  <div class="brand">
    <span class="brand__square"></span>
    <span class="brand__name">Brackenfield Prime<br>Healthcare</span>
  </div>
</section>

<section class="card card--back" aria-label="Card back">
  <svg class="back__wave" width="620" height="354" viewBox="0 0 620 354">
    <path d="M0 0 H258 C210 60 240 140 290 200 C330 250 340 300 320 354 H0 Z" fill="var(--blue)"/>
    <path d="M272 0 C232 60 258 140 306 200 C346 250 356 300 338 354" fill="none" stroke="var(--purple)" stroke-width="5"/>
  </svg>

  <div class="person">
    <p class="person__name">Daniel Harlow</p>
    <p class="person__role">Owner / C.E.O</p>
  </div>

  <ul class="contacts">
    <li>
      <svg width="11" height="11" viewBox="0 0 12 12"><circle cx="6" cy="6" r="6" fill="#fff"/><path d="M3 6.5 L6 3.5 L9 6.5 V9 H3 Z" fill="var(--blue)"/></svg>
      <span>Suite # 410, Fern Bldg,<br>IL 60404</span>
    </li>
    <li>
      <svg width="11" height="11" viewBox="0 0 12 12"><circle cx="6" cy="6" r="6" fill="#fff"/><path d="M4 3 L5.2 3 L5.8 4.8 L5 5.4 C5.4 6.4 5.8 6.8 6.6 7.2 L7.2 6.4 L9 7 V8.2 C6 8.6 3.6 6 4 3 Z" fill="var(--blue)"/></svg>
      <span>555-204-7731</span>
    </li>
    <li>
      <svg width="11" height="11" viewBox="0 0 12 12"><circle cx="6" cy="6" r="6" fill="#fff"/></svg>
      <span>555-318-2264</span>
    </li>
    <li>
      <svg width="11" height="11" viewBox="0 0 12 12"><circle cx="6" cy="6" r="6" fill="#fff"/></svg>
      <span>555-642-9108</span>
    </li>
    <li>
      <svg width="11" height="11" viewBox="0 0 12 12"><circle cx="6" cy="6" r="6" fill="#fff"/><rect x="3" y="4" width="6" height="4.2" fill="var(--blue)"/><path d="M3 4 L6 6.4 L9 4" fill="none" stroke="#fff" stroke-width="0.8"/></svg>
      <span>info@brackenfieldprime.com</span>
    </li>
    <li>
      <svg width="11" height="11" viewBox="0 0 12 12"><circle cx="6" cy="6" r="6" fill="#fff"/><circle cx="6" cy="6" r="3" fill="none" stroke="var(--blue)" stroke-width="1"/><path d="M3 6 H9" stroke="var(--blue)" stroke-width="0.8"/></svg>
      <span>www.brackenfieldprime.com</span>
    </li>
  </ul>

  <div class="brand">
    <span class="brand__square"></span>
    <span class="brand__name">Brackenfield Prime<br>Healthcare</span>
  </div>
</section>

</body>
</html>
```